依頼詳細
学習塾の看板デザインをお願いします。
基板となるイメージはできていますので、
それをブラッシュアップしてもらいたいです。
写真が二種類あり、同じデザインで、写真を差し替えたバージョンを作ってください。
記載項目
会社名等 添付ファイル参照
サイズ 横1000縦1500
希望イメージ
シンプル 複雑
単色 カラフル
暗い 明るい
日常 高級
遊び心 厳粛
未来的 伝統的
女性的 男性的
希望する色
青系、水色系
納品ファイル
• イラストレーター形式 (.ai)
補足説明
ポイント

①習慣は才能を超える、というキャッチフレーズを中心に、スタイリッシュでおしゃれなんだけど、情熱が伝わってくるデザインに仕上げて欲しい。情熱は、細部へのこだわりで伝わってくるものと思っています。

②勉強は、将来のために、今できることを毎日コツコツ積み上げていく作業。
「習慣は才能を超える」という言葉は、それを実行していくためのマインドセット。
フリータイム個別指導というのは、それを支えるための仕組み。
一般の個別指導では、時間が限られていて、本人任せの部分が大きく、サポートしきれない。
ふゆもりは、それぞれの都合に合わせていつでも毎日でも通える。
小中高一貫指導で、やる気さえあれば、どこまでもフォローできるオンリーワンの塾。
そのことを、言葉ではなく、デザインで伝えられる看板にしたい。

③原案には、上記のような思いを込めているが、自分で表現できるものには限界を感じている。
プロの手を借りて、一歩先の、情熱のこもったデザインをお願いします。
追記
・シンプルだけど、細部にこだわり、丁寧に作りこまれているものを希望します。
設置場所の写真を添付しました。
これまでのご提案を見て

シンプルなもの2点
どちらかが良いなと考えています

これからご提案頂く方へ

よりシンプル、かつ
素人では作れない
他との差別化ができているデザイン
を希望します。
■ 選んだ理由

他との違いが明確だった。
自分では全くおもいつかないデザインだった。

■ 提案者全員のお礼・コメント

この度は、ご提案と修正等の迅速な対応、誠にありがとうございました。
デザインには大変満足しております。
また、何かあった時には、お願いしたいと思っています。

```html
<!DOCTYPE html>
<html lang="ja">
<head>
<meta charset="UTF-8">
<title>学習塾ふゆもり 看板</title>
<link href="https://fonts.googleapis.com/css2?family=Noto+Sans+JP:wght@500;700;900&family=Noto+Serif+JP:wght@500&display=swap" rel="stylesheet">
<style>
  :root {
    --brand-blue: #1f4d9e;
    --deep-blue: #17387a;
    --paper: #ffffff;
    --ink: #1a2a4a;
    --photo-light: #dfe6ee;
    --photo-mid: #9aa8bd;
    --photo-dark: #2a3550;
  }
  html, body { margin: 0; padding: 0; overflow: hidden; }
  body { width: 771px; height: 1200px; background: var(--paper); }
  .signboard {
    position: relative; width: 771px; height: 1200px;
    background: var(--paper); overflow: hidden;
    font-family: "Noto Sans JP", sans-serif; color: var(--brand-blue);
  }
  .side-column {
    position: absolute; top: 0; right: 0; width: 244px; height: 1200px;
    background: var(--brand-blue);
  }
  .headline-lead {
    position: absolute; left: 34px; top: 22px; margin: 0;
    font-size: 62px; font-weight: 900; letter-spacing: 2px; line-height: 80px;
    color: var(--brand-blue);
  }
  .headline-accent {
    position: absolute; right: 22px; top: 18px; margin: 0;
    font-size: 78px; font-weight: 900; letter-spacing: 4px; line-height: 88px;
    color: var(--paper);
  }
  .hero-photo {
    position: absolute; left: 26px; top: 123px; width: 745px; height: 725px;
    border-radius: 26px 0 0 0;
    background: linear-gradient(135deg, var(--photo-light) 0%, #c9d3df 45%, var(--photo-mid) 70%, var(--photo-dark) 100%);
  }
  .campus-line {
    position: absolute; left: 52px; top: 872px; margin: 0;
    font-size: 24px; font-weight: 700; color: var(--ink); letter-spacing: 1px;
  }
  .brand {
    position: absolute; left: 26px; top: 918px; display: flex; align-items: center; gap: 22px;
  }
  .brand-mark { width: 78px; height: 78px; border: 3px solid var(--brand-blue); box-sizing: border-box; }
  .brand-name {
    font-family: "Noto Serif JP", serif; font-weight: 500; color: var(--ink);
    display: flex; flex-direction: column; align-items: center; line-height: 1;
  }
  .brand-name .latin { font-size: 46px; letter-spacing: 3px; }
  .brand-name .kana { font-size: 20px; margin-top: 8px; letter-spacing: 2px; }
  .contact { position: absolute; left: 18px; top: 1098px; color: var(--deep-blue); }
  .phone {
    display: flex; align-items: center; gap: 8px; margin: 0;
    font-size: 44px; font-weight: 700; letter-spacing: 1px; line-height: 54px;
  }
  .phone svg { width: 34px; height: 34px; }
  .access { margin: 4px 0 0 10px; font-size: 26px; font-weight: 700; color: var(--ink); }
  .service-name {
    position: absolute; right: 0; width: 244px; top: 898px; margin: 0; text-align: center;
    font-size: 36px; font-weight: 700; color: var(--paper); letter-spacing: 1px;
  }
  .service-badge {
    position: absolute; left: 572px; top: 1012px; width: 160px; height: 158px;
    background: var(--paper); border-radius: 30px;
    display: flex; align-items: center; justify-content: center; text-align: center;
    font-size: 44px; font-weight: 900; line-height: 58px; color: var(--brand-blue); letter-spacing: 2px;
  }
</style>
</head>
<body>
<main class="signboard">
  <div class="side-column"></div>
  <h1 class="headline-lead">習慣は才能を</h1>
  <p class="headline-accent">超える</p>
  <div class="hero-photo" role="img" aria-label="制服姿の生徒が机に向かいペンで問題に取り組む写真"></div>
  <p class="campus-line">小中高一貫　東町 / 北山 / 南台</p>
  <div class="brand">
    <div class="brand-mark"></div>
    <div class="brand-name"><span class="latin">FUYUMORI</span><span class="kana">学習塾ふゆもり</span></div>
  </div>
  <div class="contact">
    <p class="phone">
      <svg viewBox="0 0 24 24" aria-hidden="true"><path fill="currentColor" d="M6.6 10.8a15.1 15.1 0 0 0 6.6 6.6l2.2-2.2c.3-.3.7-.4 1-.2 1.1.4 2.3.6 3.6.6.6 0 1 .4 1 1V20c0 .6-.4 1-1 1A17 17 0 0 1 3 4c0-.6.4-1 1-1h3.5c.6 0 1 .4 1 1 0 1.3.2 2.5.6 3.6.1.3 0 .7-.2 1z"/></svg>
      052-000-4817
    </p>
    <p class="access">桜ヶ丘駅 3 番出口すぐ</p>
  </div>
  <p class="service-name">フリータイム</p>
  <div class="service-badge">個別<br>指導</div>
</main>
</body>
</html>
```